Contemporary Media Company with Logo Needs Business Card Design

Need a modern card design for a full service digital media company using the logo included. Also want the info below on the card. Probably list the services on the card back to save space for the front. Want something contemporary to impress prospective clients. You may want to submit both a somewhat more conservative design, and then a more wild one.
General Info: (this phrase need not be on the card)
Tod Parvin
Founder and CEO
949-628-4513
tod@lumavantstudio.example
lumavantstudio.example
Services: (this word need not be on the card)
Content & Experience Strategy
Brand Development
Search Engine Optimization
Website Design
Website Operation
Social Media Integration
Complete Video Solutions
Industry/Entity Type
Business
Contact Information for Business Card
Tod Parvin
Founder and CEO
949-628-4513
tod@lumavantstudio.example
lumavantstudio.example
Brand Development
Website Design
Website Operation
Social Media Integration
Complete Video Solutions
Look and feel

```html
<!DOCTYPE html>
<html lang="en">
<head>
<meta charset="UTF-8">
<title>Lumavant Studio – Business Card</title>
<link rel="stylesheet" href="https://fonts.googleapis.com/css2?family=Open+Sans:wght@400;600&display=swap">
<style>
  :root {
    --bg: #ececec;
    --card-white: #ffffff;
    --card-dark: #3a3a3a;
    --ink-grey: #5a5a5a;
    --ink-soft: #8a8a8a;
    --accent-orange: #f0822a;
    --text-light: #ffffff;
    --text-soft: #d9d9d9;
  }
  * { margin: 0; padding: 0; box-sizing: border-box; }
  html, body {
    width: 1200px;
    height: 1039px;
    overflow: hidden;
    background: var(--bg);
    font-family: "Open Sans", Arial, sans-serif;
  }
  .stage {
    position: relative;
    width: 1200px;
    height: 1039px;
  }
  .card {
    position: absolute;
    left: 250px;
    width: 700px;
    height: 400px;
    background: var(--card-white);
    box-shadow: 0 10px 28px rgba(0,0,0,0.14);
    overflow: hidden;
  }
  .card--front { top: 80px; }
  .card--back  { top: 559px; display: flex; }

  .wordmark {
    display: flex;
    align-items: center;
    gap: 16px;
  }
  .wordmark__square {
    width: 34px;
    height: 34px;
    background: var(--accent-orange);
    flex: none;
  }
  .wordmark__name {
    color: var(--ink-grey);
    font-weight: 400;
    font-size: 34px;
    letter-spacing: 4px;
    line-height: 1.05;
    text-transform: uppercase;
  }
  .card--front .wordmark {
    position: absolute;
    left: 50%;
    top: 50%;
    transform: translate(-50%, -50%);
  }

  .back__band {
    width: 96px;
    background: var(--card-dark);
  }
  .back__brand {
    width: 264px;
    display: flex;
    flex-direction: column;
    align-items: center;
    justify-content: center;
    gap: 26px;
  }
  .back__brand .wordmark { gap: 10px; }
  .back__brand .wordmark__square { width: 22px; height: 22px; }
  .back__brand .wordmark__name { font-size: 21px; letter-spacing: 2.5px; }

  .services {
    list-style: none;
    text-align: center;
    color: var(--ink-soft);
    font-size: 11px;
    line-height: 1.6;
  }

  .back__info {
    flex: 1;
    background: var(--card-dark);
    color: var(--text-light);
    padding: 92px 30px 0 38px;
  }
  .info__name {
    font-size: 28px;
    font-weight: 600;
    line-height: 1.1;
  }
  .info__title {
    font-size: 14px;
    color: var(--text-soft);
    margin-top: 4px;
  }
  .info__contacts {
    list-style: none;
    margin-top: 26px;
  }
  .info__contacts li {
    display: flex;
    align-items: center;
    gap: 12px;
    font-size: 16px;
    line-height: 1;
    margin-bottom: 11px;
  }
  .icon {
    width: 20px;
    height: 20px;
    flex: none;
  }
</style>
</head>
<body>
<main class="stage">

  <section class="card card--front" aria-label="Business card front">
    <div class="wordmark">
      <span class="wordmark__square"></span>
      <span class="wordmark__name">Lumavant<br>Studio</span>
    </div>
  </section>

  <section class="card card--back" aria-label="Business card back">
    <div class="back__band"></div>
    <div class="back__brand">
      <div class="wordmark">
        <span class="wordmark__square"></span>
        <span class="wordmark__name">Lumavant<br>Studio</span>
      </div>
      <ul class="services">
        <li>Content &amp; Experience Strategy</li>
        <li>Brand Development</li>
        <li>Search Engine Optimization</li>
        <li>Website Design</li>
        <li>Website Operation</li>
        <li>Social Media Integration</li>
        <li>Complete Video Solutions</li>
      </ul>
    </div>
    <div class="back__info">
      <p class="info__name">Tod Parvin</p>
      <p class="info__title">Founder and CEO</p>
      <ul class="info__contacts">
        <li>
          <svg class="icon" viewBox="0 0 20 20" aria-hidden="true"><circle cx="10" cy="10" r="10" fill="#fff"/><path d="M6.5 5.5h2l1 2.5-1.3 1a6 6 0 0 0 2.8 2.8l1-1.3 2.5 1v2a1 1 0 0 1-1 1A8.5 8.5 0 0 1 5.5 6.5a1 1 0 0 1 1-1z" fill="#3a3a3a"/></svg>
          949-628-4513
        </li>
        <li>
          <svg class="icon" viewBox="0 0 20 20" aria-hidden="true"><circle cx="10" cy="10" r="10" fill="#fff"/><rect x="5" y="6.5" width="10" height="7" fill="#3a3a3a"/><path d="M5.5 7l4.5 3.5L14.5 7" stroke="#fff" stroke-width="1" fill="none"/></svg>
          tod@lumavantstudio.example
        </li>
        <li>
          <svg class="icon" viewBox="0 0 20 20" aria-hidden="true"><circle cx="10" cy="10" r="10" fill="#fff"/><circle cx="10" cy="10" r="5" fill="none" stroke="#3a3a3a" stroke-width="1.3"/><path d="M5 10h10M10 5c-2 3-2 7 0 10M10 5c2 3 2 7 0 10" stroke="#3a3a3a" stroke-width="1" fill="none"/></svg>
          lumavantstudio.example
        </li>
      </ul>
    </div>
  </section>

</main>
</body>
</html>
```